Marrowfield Benefit Advisors Business Card Design

I already placed order for cards through sketch hive.

Double sided- back Navy with White logo and raised silver "swoosh"

```html
<!DOCTYPE html>
<html lang="en">
<head>
<meta charset="utf-8">
<title>Marrowfield Benefit Advisors – Business Card</title>
<link href="https://fonts.googleapis.com/css2?family=Cinzel:wght@500;600&family=Poppins:wght@400;500&display=swap" rel="stylesheet">
<style>
  :root {
    --navy: #13244a;
    --white: #ffffff;
    --silver: #a9abae;
    --ink: #1b2b52;
    --text-grey: #4a4f5a;
    --stage: #3a3a3c;
  }
  * { margin: 0; padding: 0; box-sizing: border-box; }
  html, body { width: 1200px; height: 875px; overflow: hidden; }
  body {
    background: var(--stage);
    position: relative;
    font-family: "Poppins", sans-serif;
  }
  .card {
    position: absolute;
    top: 288px;
    width: 520px;
    height: 298px;
    border-radius: 18px;
    overflow: hidden;
  }
  .card--back { left: 50px; background: var(--navy); }
  .card--front { left: 630px; background: var(--white); }

  /* back side */
  .back-lockup {
    position: absolute;
    left: 0; right: 0; top: 50%;
    transform: translateY(-50%);
    display: flex;
    align-items: center;
    justify-content: center;
    gap: 14px;
  }
  .back-lockup__dot {
    width: 18px; height: 18px;
    border-radius: 50%;
    background: var(--white);
  }
  .back-lockup__name {
    font-family: "Cinzel", serif;
    font-weight: 600;
    color: var(--white);
    font-size: 25px;
    line-height: 1.15;
    letter-spacing: 1px;
  }
  .back-lockup__name span { display: block; font-size: 13px; letter-spacing: 5px; }

  /* front side */
  .front-lockup {
    position: absolute;
    left: 40px; top: 40px;
    font-family: "Cinzel", serif;
    font-weight: 600;
    color: var(--ink);
    font-size: 30px;
    line-height: 1.1;
    letter-spacing: 1px;
  }
  .front-lockup span { display: block; font-size: 12px; letter-spacing: 6px; }
  .person {
    position: absolute;
    left: 40px; top: 132px;
  }
  .person__name {
    font-family: "Cinzel", serif;
    font-weight: 500;
    font-size: 19px;
    color: var(--ink);
  }
  .person__role { font-size: 11px; color: var(--text-grey); }
  .address {
    position: absolute;
    left: 40px; top: 182px;
    font-size: 11px;
    line-height: 1.4;
    color: var(--ink);
  }
  .contacts {
    position: absolute;
    left: 40px; top: 224px;
    list-style: none;
    font-size: 11px;
    color: var(--ink);
  }
  .contacts li { display: flex; align-items: center; gap: 8px; line-height: 1.55; }
  .contacts svg { width: 10px; height: 10px; fill: var(--ink); flex: none; }
  .accent-tab {
    position: absolute;
    left: 0; top: 176px;
    width: 5px; height: 30px;
    background: var(--navy);
  }
</style>
</head>
<body>
  <section class="card card--back" aria-label="Card back">
    <div class="back-lockup">
      <div class="back-lockup__dot"></div>
      <div class="back-lockup__name">MARROWFIELD<span>BENEFIT ADVISORS</span></div>
    </div>
  </section>

  <section class="card card--front" aria-label="Card front">
    <div class="front-lockup">MARROWFIELD<span>BENEFIT ADVISORS</span></div>
    <div class="accent-tab"></div>
    <div class="person">
      <p class="person__name">Lena Hartwell</p>
      <p class="person__role">CEO &amp; Founder</p>
    </div>
    <p class="address">42 Alder Court Plaza<br>Brookhaven, NJ 07100 USA</p>
    <ul class="contacts">
      <li><svg viewBox="0 0 10 10"><path d="M2 0h2l1 2.5-1.3 1a5 5 0 0 0 2.8 2.8l1-1.3L10 6v2a2 2 0 0 1-2 2A8 8 0 0 1 0 2a2 2 0 0 1 2-2z"/></svg>+1.555.010.234</li>
      <li><svg viewBox="0 0 10 10"><path d="M0 2h10v6H0z M0 2l5 3.5L10 2" stroke="#fff" stroke-width=".8"/></svg>info@marrowfieldadvisors.com</li>
      <li><svg viewBox="0 0 10 10"><circle cx="5" cy="5" r="5"/><path d="M0 5h10M5 0c-2 3-2 7 0 10M5 0c2 3 2 7 0 10" stroke="#fff" stroke-width=".7" fill="none"/></svg>www.marrowfieldadvisors.com</li>
    </ul>
  </section>
</body>
</html>
```